Business Card Design using new attached logo

We are a family run Plumbing and Heating firm looking to improve our company image with an improved business card and new logo.We are looking to keep the company colour (Blue) involved in our design

Reason: New logo added which needs to be incorporated on designs

Industry/Entity Type

Business

Contact Information for Business Card

See attachment of all info required.

Requirements
Must have
• We have just picked a new company logo which is attached.
• Could you please provide your business card designs using this logo.
• We are looking for the logo on the back as well as the front with all the info required

```html
<!DOCTYPE html>
<html lang="en">
<head>
<meta charset="utf-8">
<title>Kelvane Heating Ltd. – Business Cards</title>
<link rel="stylesheet" href="https://fonts.googleapis.com/css2?family=Oswald:wght@600&family=Questrial&display=swap">
<style>
  :root {
    --brand-blue: #11a9e8;
    --brand-blue-deep: #0a95d6;
    --card-white: #ffffff;
    --ink-grey: #6d6e71;
    --ink-dark: #58595b;
    --backdrop: #e9e9e7;
  }
  * { margin: 0; padding: 0; box-sizing: border-box; }
  html, body {
    width: 1200px; height: 856px; overflow: hidden;
    background: var(--backdrop);
  }
  .canvas { position: relative; width: 1200px; height: 856px; }

  .card {
    position: absolute;
    width: 560px; height: 320px;
    border-radius: 34px;
    box-shadow: 0 10px 28px rgba(0,0,0,0.12);
  }

  /* Back of card */
  .card--back {
    left: 560px; top: 80px;
    background: var(--brand-blue);
    color: var(--card-white);
    font-family: "Questrial", sans-serif;
    text-align: center;
  }
  .back-mark {
    position: absolute; left: 50%; top: 60px;
    width: 120px; height: 120px; margin-left: -60px;
    border-radius: 50%; background: var(--card-white);
  }
  .back-address {
    position: absolute; left: 0; right: 0; top: 214px;
    font-size: 15px; letter-spacing: 0.3px; line-height: 1.5;
    font-style: normal;
  }
  .back-lines { display: flex; justify-content: center; gap: 6px; align-items: center; }
  .icon { width: 14px; height: 14px; vertical-align: -2px; margin-right: 3px; }

  /* Front of card */
  .card--front {
    left: 150px; top: 440px;
    background: var(--card-white);
    font-family: "Questrial", sans-serif;
    color: var(--ink-grey);
  }
  .front-mark {
    position: absolute; left: 50px; top: 94px;
    width: 140px; height: 140px;
    border-radius: 50%; background: var(--brand-blue);
  }
  .company-name {
    position: absolute; left: 218px; top: 96px;
    font-family: "Oswald", sans-serif; font-weight: 600;
    font-size: 29px; line-height: 1; letter-spacing: 0;
    color: var(--brand-blue);
    text-transform: uppercase;
    white-space: nowrap;
  }
  .contact { position: absolute; left: 220px; top: 142px; }
  .contact-name {
    font-weight: 700; font-size: 17px; letter-spacing: 0.6px;
    color: var(--ink-dark); text-transform: uppercase;
    line-height: 1.2;
  }
  .contact-role { font-size: 14px; margin-top: 2px; line-height: 1.2; }
  .contact-line { font-size: 17px; margin-top: 4px; color: var(--ink-dark); line-height: 1.2; white-space: nowrap; }
  .contact-line .icon { fill: var(--ink-dark); }
</style>
</head>
<body>
<main class="canvas">

  <section class="card card--back" aria-label="Back of business card">
    <div class="back-mark"></div>
    <address class="back-address">
      <div>14 Mill Row, Elmfield Road, Harwick, Surrey HW2 5LT</div>
      <div class="back-lines">
        <span><svg class="icon" viewBox="0 0 16 16" fill="#fff"><circle cx="8" cy="8" r="8"/><path d="M5 4.2l1.6-.4.9 2-1 .8a5 5 0 0 0 2.3 2.3l.8-1 2 .9-.4 1.6c-3.4.3-6.5-2.8-6.2-6.2z" fill="#11a9e8"/></svg>020 7946 0321</span>
        <span><svg class="icon" viewBox="0 0 16 16" fill="#fff"><circle cx="8" cy="8" r="8"/><rect x="4.5" y="6" width="7" height="5" rx="1" fill="#11a9e8"/><rect x="5.5" y="4" width="5" height="2" fill="#11a9e8"/></svg>020 7946 0872</span>
      </div>
    </address>
  </section>

  <section class="card card--front" aria-label="Front of business card">
    <div class="front-mark"></div>
    <h1 class="company-name">Kelvane Heating Ltd.</h1>
    <div class="contact">
      <p class="contact-name">Daniel Marsh</p>
      <p class="contact-role">Director</p>
      <p class="contact-line"><svg class="icon" viewBox="0 0 16 16"><circle cx="8" cy="8" r="8"/><path d="M5 4.2l1.6-.4.9 2-1 .8a5 5 0 0 0 2.3 2.3l.8-1 2 .9-.4 1.6c-3.4.3-6.5-2.8-6.2-6.2z" fill="#fff"/></svg>07700 900123</p>
      <p class="contact-line"><svg class="icon" viewBox="0 0 16 16"><circle cx="8" cy="8" r="8"/><rect x="4" y="5.5" width="8" height="5" rx="0.8" fill="#fff"/><path d="M4.3 5.8L8 8.6l3.7-2.8" stroke="#58595b" stroke-width="0.9" fill="none"/></svg>d.marsh@kelvaneheating.co.uk</p>
    </div>
  </section>

</main>
</body>
</html>
```